Web Design for photo printing service

Hi
I am looking for a new web design theme for our almost ready website http://fotoblik.zrmq.net, it will soon be launched under the name: www.zuna.is. (ZUNA means: You Only Live Once)

This is a website focused on printing photo products like: photo books, Greeting cards, posters, etc.

The whole theme should be playful, fun, creative. The marketing will be is that Life is fun, keep your memories. remember the good time etc.

So what I am looking for is a simple, yet colorful theme, easy to use.

We will be running max 4- 6 product groups, all extra info should be on the button,
expect shopping chart and sign in should be on top.

Extra feature:
Once a year during christmas, the web will turn on christmas outfit, it transforms
to Christmas looking Web. So a X-mas version would be fun to see !

Target Market(s)

Young people 20-35, young families.

Industry/Entity Type

Printing

Requirements
Must have
• Fun looking colorful design, simple to use.
Should not have
• Dark heavy look

```html
<!DOCTYPE html>
<html lang="is">
<head>
<meta charset="utf-8">
<title>ZUNA – ljósmyndaprentun</title>
<link rel="stylesheet" href="https://fonts.googleapis.com/css2?family=Questrial&display=swap">
<style>
:root{
  --blue:#0aa1c9;
  --purple:#9b2a8c;
  --orange:#f6943f;
  --teal:#1a9a7a;
  --green:#a8cf45;
  --pink:#e3388a;
  --white:#ffffff;
  --ink:#555555;
  --silver:#b9b9b9;
}
*{box-sizing:border-box;margin:0;padding:0}
html,body{width:1010px;height:1200px;overflow:hidden;background:var(--white)}
body{font-family:"Questrial",sans-serif;position:relative;color:var(--ink)}
.top-stripe{position:absolute;left:0;top:0;width:1010px;height:6px;
  background:repeating-linear-gradient(90deg,var(--purple) 0 22px,var(--orange) 22px 44px,var(--blue) 44px 66px,var(--green) 66px 88px,var(--pink) 88px 110px)}
.brand{position:absolute;left:84px;top:62px;display:flex;align-items:center;gap:10px}
.brand-dot{width:22px;height:22px;border-radius:50%;background:var(--pink)}
.brand-name{font-size:58px;color:var(--blue);letter-spacing:2px;line-height:1}
.cart{position:absolute;left:737px;top:35px;width:165px;height:110px;
  background:linear-gradient(135deg,#e9e9e9,#9c9c9c);border:1px solid #8c8c8c;padding:14px 16px}
.cart::before{content:"";position:absolute;left:68px;top:-20px;width:30px;height:20px;
  border-left:1px solid #777;border-right:1px solid #777;transform:none;
  clip-path:polygon(50% 0,100% 100%,0 100%);background:transparent}
.cart-hook{position:absolute;left:80px;top:-22px;width:7px;height:7px;border-radius:50%;background:#777}
.cart-wire{position:absolute;left:66px;top:-18px;width:34px;height:18px}
.cart-board{width:100%;height:100%;background:var(--green);border:2px solid #d6d6d6;
  text-align:center;color:var(--white);padding-top:8px;font-size:11px;line-height:15px}
.cart-title{color:#4d5a2a;font-size:12px}
.cart-meta{color:#4d5a2a;font-size:9px}
.main-nav{position:absolute;left:81px;top:166px;display:flex;height:50px}
.main-nav a{display:flex;align-items:center;justify-content:center;color:var(--white);
  text-decoration:none;font-size:13px;text-transform:uppercase;height:50px;position:relative}
.main-nav .active::after{content:"";position:absolute;bottom:-12px;left:64px;border:8px solid transparent;border-top:6px solid var(--blue);border-bottom:0;width:0}
.hero{position:absolute;left:81px;top:216px;width:824px;height:375px;overflow:hidden}
.hero svg{display:block}
.hero-arrow{position:absolute;top:140px;width:40px;height:50px;background:var(--white);display:flex;align-items:center;justify-content:center}
.hero-arrow.prev{left:-12px;border-radius:0 25px 25px 0}
.hero-arrow.next{right:-12px;border-radius:25px 0 0 25px}
.hero-caption{position:absolute;left:15px;top:242px;width:330px;height:128px;background:var(--pink);
  clip-path:polygon(0 0,92% 0,100% 100%,0 100%);color:var(--white);padding:14px 18px}
.hero-caption h2{font-weight:400;font-size:15px;margin-bottom:12px}
.hero-caption p{font-size:10.5px;line-height:16px}
.products{position:absolute;left:111px;top:617px;display:grid;grid-template-columns:repeat(3,248px);gap:13px 13px}
.product{position:relative;height:214px;border-radius:6px;padding:6px;color:var(--white)}
.product-photo{height:130px;position:relative}
.product-photo::after{content:"";position:absolute;left:86px;bottom:0;border:10px solid transparent;border-bottom-color:inherit;border-top:0}
.product h3{font-weight:400;font-size:12.5px;margin:16px 0 3px 8px;text-transform:uppercase}
.product p{font-size:9.5px;line-height:15px;margin:0 8px;text-align:justify}
.ribbon-wrap{position:absolute;right:-8px;top:-8px;width:112px;height:112px;overflow:hidden}
.ribbon{position:absolute;right:-34px;top:30px;width:150px;height:26px;transform:rotate(45deg);
  color:var(--white);font-size:11px;text-align:center;line-height:26px;box-shadow:0 2px 3px rgba(0,0,0,.25)}
.c-blue{background:var(--blue)} .c-purple{background:var(--purple)} .c-orange{background:var(--orange)}
.c-teal{background:var(--teal)} .c-green{background:var(--green)}
.footer{position:absolute;left:0;top:1108px;width:1010px;height:92px;background:var(--blue)}
.footer-edge{position:absolute;left:0;top:-6px;width:1010px;height:7px;
  background:linear-gradient(135deg,var(--blue) 33%,transparent 33%) 0 0/8px 8px,
             linear-gradient(225deg,var(--blue) 33%,transparent 33%) 0 0/8px 8px}
.footer-nav{position:absolute;left:129px;top:41px;display:flex;font-size:11px;color:var(--white)}
.footer-nav a{color:var(--white);text-decoration:none}
.footer-nav .sep{margin:0 17px}
.social{position:absolute;left:790px;top:32px;display:flex;gap:6px}
.social span{width:30px;height:30px;border-radius:50%;display:block}
</style>
</head>
<body>
<div class="top-stripe"></div>

<header>
  <div class="brand"><span class="brand-name">ZUNA</span><span class="brand-dot"></span></div>
  <div class="cart">
    <svg class="cart-wire" viewBox="0 0 34 18"><path d="M1 18 L17 2 L33 18" fill="none" stroke="#777" stroke-width="1"/><circle cx="17" cy="3" r="3" fill="#777"/></svg>
    <div class="cart-board">
      <div class="cart-title">Karfan mín</div>
      <div class="cart-meta">0 articles • kr 0,00</div>
      <div style="margin-top:6px">Stofna reikning</div>
      <div>Skrá inn</div>
    </div>
  </div>
  <nav class="main-nav">
    <a class="c-blue active" style="width:145px">Ljósmyndabækur</a>
    <a class="c-purple" style="width:106px">Dagatöl</a>
    <a class="c-orange" style="width:118px">Veggspjöld</a>
    <a class="c-teal" style="width:138px">Tækifæriskort</a>
    <a class="c-green" style="width:189px">Prentaðar ljósmyndir</a>
    <a style="width:127px;background:var(--pink)">Verðin okkar</a>
  </nav>
</header>

<section class="hero">
  <svg width="824" height="375" viewBox="0 0 824 375">
    <defs>
      <linearGradient id="heroPhoto" x1="0" y1="0" x2="0" y2="1">
        <stop offset="0" stop-color="#2f7fd6"/>
        <stop offset=".35" stop-color="#8fb9e6"/>
        <stop offset=".6" stop-color="#e7b98f"/>
        <stop offset="1" stop-color="#e56d2c"/>
      </linearGradient>
    </defs>
    <rect width="824" height="375" fill="#a8cf45"/>
    <ellipse cx="422" cy="170" rx="322" ry="340" fill="#0aa1c9"/>
    <ellipse cx="432" cy="170" rx="322" ry="340" fill="#1fc08e"/>
    <ellipse cx="426" cy="170" rx="314" ry="334" fill="#ffffff"/>
    <ellipse cx="426" cy="170" rx="306" ry="328" fill="url(#heroPhoto)" role="img" aria-label="Photo of smiling children against a blue sky"/>
  </svg>
  <div class="hero-arrow prev"><svg width="20" height="24" viewBox="0 0 20 24"><path d="M15 2 L5 12 L15 22" fill="none" stroke="#a8cf45" stroke-width="6"/></svg></div>
  <div class="hero-arrow next"><svg width="20" height="24" viewBox="0 0 20 24"><path d="M5 2 L15 12 L5 22" fill="none" stroke="#a8cf45" stroke-width="6"/></svg></div>
  <div class="hero-caption">
    <h2>HEADING TITLE GOES HERE</h2>
    <p>Lorem ipsum dolor sit amet, consectetur adipiscing elit. Quisque consequat sapien nec lectus congue pellentesque. Aliquam et adipiscing metus. Proin id erat ut urna feugiat euismod.</p>
  </div>
</section>

<main class="products">
  <article class="product c-blue">
    <div class="product-photo" role="img" aria-label="Photo of an open photo book with snowy landscapes" style="background:linear-gradient(135deg,#dfe6ea,#7d94a3);border-bottom-color:var(--blue)"></div>
    <h3>Ljósmyndabækur</h3>
    <p>Þín eigin ljósmyndabók? Af hverju ekki? Við vitum að þínar myndir eiga það skilið að</p>
    <div class="ribbon-wrap"><div class="ribbon" style="background:#c2346f">know more</div></div>
  </article>
  <article class="product c-purple">
    <div class="product-photo" role="img" aria-label="Photo of wall calendars with colourful pictures" style="background:linear-gradient(135deg,#9ab86a,#dcdcdc);border-bottom-color:var(--purple)"></div>
    <h3>Dagatöl</h3>
    <p>Dagatölin okkar eru einstaklega skemmtileg aflestar, sérstaklega laugardagarnir.</p>
    <div class="ribbon-wrap"><div class="ribbon" style="background:#16785e">know more</div></div>
  </article>
  <article class="product c-orange">
    <div class="product-photo" role="img" aria-label="Photo of children lying on the floor" style="background:linear-gradient(135deg,#e9d8c4,#b86b4a);border-bottom-color:var(--orange)"></div>
    <h3>Veggspjöld</h3>
    <p>Veggspjöldin okkar eru prentuð á glæsilegan 170 gramma pappír. Sem þýðir að þetta</p>
    <div class="ribbon-wrap"><div class="ribbon" style="background:#6e9a2c">know more</div></div>
  </article>
  <article class="product c-teal">
    <div class="product-photo" role="img" aria-label="Photo collage greeting card with family pictures" style="background:linear-gradient(135deg,#8a2a22,#3f6b3a);border-bottom-color:var(--teal)"></div>
    <h3>Tækifæriskort</h3>
    <p>Jól, afmæli, ferming, gifting eða hvaða tilefni sem er. Það er alltaf gaman að fá kort.</p>
    <div class="ribbon-wrap"><div class="ribbon" style="background:#0a86a8">know more</div></div>
  </article>
  <article class="product c-green">
    <div class="product-photo" role="img" aria-label="Photo of a stack of printed photographs" style="background:linear-gradient(135deg,#f0f0f0,#6b6b6b);border-bottom-color:var(--green)"></div>
    <h3>Prentaðar ljósmyndir</h3>
    <p>Ljósmyndir í öllum stærðum og gerðum prentaðar eftir þínum hentugleika.</p>
    <div class="ribbon-wrap"><div class="ribbon" style="background:#d9782c">know more</div></div>
  </article>
</main>

<footer class="footer">
  <div class="footer-edge"></div>
  <nav class="footer-nav">
    <a>Heim</a><span class="sep">|</span>
    <a>Smáa letrið</a><span class="sep">|</span>
    <a>Hvað viltu vita</a><span class="sep">|</span>
    <a>Verð</a><span class="sep">|</span>
    <a>Um okkur</a><span class="sep">|</span>
    <a>Samband</a>
  </nav>
  <div class="social" aria-label="Social links">
    <span style="background:var(--orange)"></span>
    <span style="background:#3b5b9a"></span>
    <span style="background:#5aa6de"></span>
    <span style="background:#1f6fa8"></span>
  </div>
</footer>
</body>
</html>
```